KRT World Class Organisation Poster

We are looking for ideas on how to design this poster to best capture the message we are trying to convey (KRT World Class Organisation). Make sure that these 5 statements feature on the poster.

Logo has been provided, please include in your poster design.

Please use the logo design as the inspiration for your poster layout, drawing on the DNA double helix symbol.

Also refer to the layout of the attached poster. We would like to retain the layout however it should be visually appealing - use your imagination & creativity!
Updates

Updated design brief & extended deadline.

Target Market(s)

internal company use only - logo provided which will need to be included.

Requirements
Must have
• The poster should be in portrait format as it will be printed in 'A3' size.

Must include the KRT logo provided - see attached file.
Nice to have
• Please use the logo design as the inspiration for your poster layout, drawing on the DNA double helix symbol.

```html
<!DOCTYPE html>
<html lang="en">
<head>
<meta charset="utf-8">
<title>World Class Organisation Poster</title>
<link href="https://fonts.googleapis.com/css2?family=Open+Sans:wght@400;600;700;800&display=swap" rel="stylesheet">
<style>
  :root {
    --band: #b3b3b3;
    --paper-light: #f6f6f6;
    --paper-mid: #e4e4e4;
    --ink: #0a0a0a;
    --blue: #1a9ad6;
    --green: #3aa826;
    --red: #ee1c25;
    --orange: #f5b400;
    --purple: #9b1ee6;
  }
  * { margin: 0; padding: 0; box-sizing: border-box; }
  html, body { width: 1200px; height: 1000px; overflow: hidden; }
  body { font-family: "Open Sans", Arial, sans-serif; color: var(--ink); }

  .poster { position: relative; width: 1200px; height: 1000px; background: var(--band); }
  .poster__field {
    position: absolute; left: 0; top: 75px; width: 1200px; height: 850px;
    background: radial-gradient(ellipse at 50% 45%, var(--paper-light) 0%, #ededed 60%, var(--paper-mid) 100%);
  }
  .poster__graphics { position: absolute; left: 0; top: 0; }

  .headline { font-family: "Open Sans", Arial, sans-serif; font-weight: 800; fill: var(--ink); }

  .verb {
    position: absolute; transform: translateX(-50%);
    font-size: 29px; font-weight: 600; line-height: 32px;
    text-align: center; white-space: nowrap;
  }

  .statement {
    position: absolute; top: 570px; width: 240px; transform: translateX(-50%);
    font-size: 24px; line-height: 24.4px; letter-spacing: -0.02em;
    text-align: center; white-space: nowrap;
  }
  .statement b { font-weight: 700; }
  .statement--blue b { color: var(--blue); }
  .statement--green b { color: var(--green); }
  .statement--red b { color: var(--red); }
  .statement--orange b { color: var(--orange); }
  .statement--purple b { color: var(--purple); }
</style>
</head>
<body>
<main class="poster">
  <div class="poster__field"></div>

  <svg class="poster__graphics" width="1200" height="1000" viewBox="0 0 1200 1000" aria-hidden="true">
    <defs>
      <filter id="lift" x="-5%" y="-5%" width="110%" height="120%">
        <feDropShadow dx="4" dy="5" stdDeviation="3" flood-color="#000" flood-opacity="0.35"/>
      </filter>
    </defs>

    <text class="headline" x="505" y="192" font-size="150" textLength="200" lengthAdjust="spacingAndGlyphs" filter="url(#lift)">we</text>

    <g class="connectors" stroke-width="6" fill="none">
      <line x1="105" y1="270" x2="213" y2="386" stroke="var(--blue)"/>
      <line x1="381" y1="270" x2="381" y2="386" stroke="var(--green)"/>
      <line x1="598" y1="207" x2="598" y2="300" stroke="var(--red)"/>
      <line x1="598" y1="365" x2="598" y2="410" stroke="var(--red)"/>
      <line x1="846" y1="270" x2="846" y2="386" stroke="var(--orange)"/>
      <line x1="1090" y1="270" x2="982" y2="386" stroke="var(--purple)"/>
    </g>

    <text class="headline" x="150" y="553" font-size="240" textLength="895" lengthAdjust="spacingAndGlyphs" filter="url(#lift)">WorldClass</text>

    <g class="underlines">
      <rect x="24" y="905" width="214" height="11" fill="var(--blue)"/>
      <rect x="260" y="905" width="214" height="11" fill="var(--green)"/>
      <rect x="493" y="905" width="214" height="11" fill="var(--red)"/>
      <rect x="727" y="905" width="214" height="11" fill="var(--orange)"/>
      <rect x="962" y="905" width="214" height="11" fill="var(--purple)"/>
    </g>
  </svg>

  <div class="verb" style="left:110px; top:200px;">Employ</div>
  <div class="verb" style="left:375px; top:200px;">Manufacture<br>Using Innovative</div>
  <div class="verb" style="left:598px; top:325px;">Strive To Be</div>
  <div class="verb" style="left:840px; top:200px;">Work With</div>
  <div class="verb" style="left:1083px; top:200px;">Believe</div>

  <p class="statement statement--blue" style="left:114px;"><b>Business</b><br>Systems to<br>exceed<br>expectations<br>by driving<br><b>innovation</b> at<br>the forefront of<br><b>technology</b>.</p>

  <p class="statement statement--green" style="left:374px;"><b>Processes</b> and<br>lean<br><b>technologies</b><br>adapted to<br>produce safe,<br>effective &amp;<br>reliable<br><b>products</b> to<br>meet our<br>patients’ needs.</p>

  <p class="statement statement--red" style="left:600px;"><b>Colleagues</b> who<br>are professional,<br>motivated,<br>helpful and<br>positive. We are<br>accountable in<br>achieving our<br>goals. We are<br>innovative,<br>always challenge<br>the status-quo<br>and open to<br>new <b>ideas</b>.</p>

  <p class="statement statement--orange" style="left:841px;">Service<br><b>Providers</b> who<br>are <b>leaders</b> and<br>innovators that<br>challenge the<br>status-quo and<br>focus<br>on quality<br>excellence and<br>continuous<br>improvement to<br>exceed customer<br>expectations.</p>

  <p class="statement statement--purple" style="left:1085px;"><b>Customer</b><br>Service is to<br>deliver the<br>ultimate<br>customer<br><b>satisfaction</b><br>every time.</p>
</main>
</body>
</html>
```